Infectious Diseases Research Laboratory Needs Business Card

We need a business card for an academic research laboratory based in Kansas City called VELKOR. The full lab name is Microbe Exposure Kinetics/Response Modeling Integrated Study Laboratory, but this does not need to be incorporated. We study novel ways to optimize the treatment of multidrug-resistant bacterial infections ("superbugs") throughout the entire biomedical research spectrum (from benchtop to bedside). The name VELKOR is not only an acronym for our lab name, but also represents our desire to make discoveries and explore the unknown (the stars, if you well). It also serves as an ode to the state of Kansas motto where we are based, ad astra per aspera ("to the stars, through difficulty").

Target Market(s)

Pharmaceutical companies, researchers

Industry/Entity Type

Pharmaceutical

Contact Information for Business Card

The business card should incorporate and complement our new logo (see uploaded files). Double-sided designs are preferred. Looking for something modern, but professional.

Font styles to use
Sans Serif

Requirements
Must have
• Double-sided. One side would ideally be a solid color incorporating logo and the other should also have the logo (smaller), but incorporate staff information.
• Color codes:
• Red: #F04C51
• Blue: #3477B5
• Gray: #808285

```html
<!DOCTYPE html>
<html lang="en">
<head>
<meta charset="utf-8">
<title>VELKOR Business Card</title>
<link href="https://fonts.googleapis.com/css2?family=Roboto:wght@400;500;700&display=swap" rel="stylesheet">
<style>
  :root {
    --red: #F04C51;
    --red-deep: #E0434B;
    --blue: #3477B5;
    --blue-deep: #2B66A1;
    --purple: #7A5A88;
    --gray: #808285;
    --ink: #2A2A2C;
    --paper: #F4F4F3;
    --white: #FFFFFF;
    --backdrop: #E6E6E6;
  }
  * { margin: 0; padding: 0; box-sizing: border-box; }
  html, body {
    width: 1200px; height: 576px; overflow: hidden;
    background: var(--backdrop);
    font-family: "Roboto", Arial, sans-serif;
  }
  .canvas { position: relative; width: 1200px; height: 576px; }

  .card {
    position: absolute; top: 138px; width: 484px; height: 294px;
    border-radius: 14px; overflow: hidden;
    box-shadow: 0 3px 8px rgba(0,0,0,.18);
  }

  /* Front */
  .card--front {
    left: 81px;
    background: linear-gradient(180deg, var(--red-deep) 0%, #B9506A 30%, var(--purple) 55%, #4A6AA0 78%, var(--blue-deep) 100%);
  }
  .brand {
    position: absolute; display: flex; align-items: center;
  }
  .brand__dot { border-radius: 50%; flex: none; }
  .brand__text { display: flex; flex-direction: column; }
  .brand__name {
    font-weight: 500; line-height: 1; letter-spacing: .04em;
  }
  .brand__sub {
    font-weight: 500; text-transform: uppercase; letter-spacing: .06em;
    white-space: nowrap; text-align: center;
  }
  .brand__sub--rule { border-top: 1px solid currentColor; padding-top: 2px; margin-top: 2px; }

  .card--front .brand { left: 88px; top: 108px; gap: 14px; }
  .card--front .brand__dot { width: 62px; height: 62px; background: var(--white); }
  .card--front .brand__name { color: var(--white); font-size: 52px; }
  .card--front .brand__sub { color: var(--white); font-size: 5.6px; margin-top: 4px; }

  /* Back */
  .card--back {
    left: 602px;
    background: linear-gradient(180deg, #FBFBFA 0%, var(--paper) 100%);
  }
  .card--back .brand { left: 30px; top: 36px; gap: 14px; }
  .card--back .brand__dot { width: 62px; height: 62px; background: var(--red); }
  .card--back .brand__name { color: var(--red); font-size: 52px; }
  .card--back .brand__sub { color: var(--gray); font-size: 5.6px; margin-top: 4px; }

  .staff { position: absolute; left: 30px; top: 208px; }
  .staff__name { color: var(--red); font-weight: 500; font-size: 21px; }
  .staff__role { color: var(--ink); font-size: 12px; margin-top: 6px; }

  .contact {
    position: absolute; left: 250px; top: 170px;
    color: var(--ink); font-size: 12.5px; line-height: 16px;
  }
  .contact__address { margin-bottom: 8px; }
  .contact__row { display: flex; align-items: center; gap: 10px; margin-bottom: 3px; }
  .contact__icon { width: 12px; height: 12px; fill: var(--red); flex: none; }

  .band-blue {
    position: absolute; left: 0; bottom: 0; width: 220px; height: 13px;
    background: var(--blue);
  }
  .band-red {
    position: absolute; right: 0; bottom: 0; width: 288px; height: 31px;
    background: var(--red);
    clip-path: polygon(14px 0, 100% 0, 100% 100%, 0 100%);
  }
  .band-red__url {
    position: absolute; left: 54px; top: 8px;
    color: var(--white); font-size: 12.5px;
  }
</style>
</head>
<body>
<main class="canvas">

  <section class="card card--front" aria-label="Card front">
    <div class="brand">
      <span class="brand__dot"></span>
      <div class="brand__text">
        <span class="brand__name">VELKOR</span>
        <span class="brand__sub">Microbe Exposure Kinetics/Response Modeling</span>
        <span class="brand__sub brand__sub--rule">Integrated Study Laboratory</span>
      </div>
    </div>
  </section>

  <section class="card card--back" aria-label="Card back">
    <div class="brand">
      <span class="brand__dot"></span>
      <div class="brand__text">
        <span class="brand__name">VELKOR</span>
        <span class="brand__sub">Microbe Exposure Kinetics/Response Modeling</span>
        <span class="brand__sub brand__sub--rule">Integrated Study Laboratory</span>
      </div>
    </div>

    <div class="staff">
      <p class="staff__name">Daniel Reyes</p>
      <p class="staff__role">Managing Director</p>
    </div>

    <div class="contact">
      <p class="contact__address">48 Meadowlark Lane Suite 7<br>Kansas City 66100</p>
      <p class="contact__row">
        <svg class="contact__icon" viewBox="0 0 24 24" aria-hidden="true"><path d="M3 9c0-3 4-5 9-5s9 2 9 5v2h-5V9c-1-1-7-1-8 0v2H3zM6 12h12l2 8H4z"/></svg>
        1800-555-0147
      </p>
      <p class="contact__row">
        <svg class="contact__icon" viewBox="0 0 24 24" aria-hidden="true"><path d="M2 5h20v14H2zM3 6l9 7 9-7v2l-9 7-9-7z" fill-rule="evenodd"/></svg>
        dreyes@velkorlab.org
      </p>
    </div>

    <div class="band-blue"></div>
    <div class="band-red"><span class="band-red__url">www.velkorlab.org</span></div>
  </section>

</main>
</body>
</html>
```